Wildlife photographer Website

The website is to be a "resume" of pictures and awards won by Nora. Lean heavy to outdoor wildlife.
She will post articles and have ability to interact with fans.

I will add some of her pictures tonight,

Target Market(s)

Terra Quarterly .....anyone looking to hire a wildlife photographer.

Industry/Entity Type

Professional Photography

Contact Information for Business Card

Nora Falkett
4817 Maple Hollow Lane
Columbia MD 21078
443-581-2094
Nora@FernOwlPix.com

Coding

Coded - Design and coding required

Number of Pages Required

5+ page

Requirements
Must have
• New Logo
Nice to have
• Nature, and eye catching graphics

```html
<!DOCTYPE html>
<html lang="en">
<head>
<meta charset="utf-8">
<title>Nora Falkett — Wildlife Photographer</title>
<link href="https://fonts.googleapis.com/css2?family=Montserrat:wght@500;600;700&family=Crimson+Text:wght@400;600;700&family=Kaushan+Script&display=swap" rel="stylesheet">
<style>
  :root{
    --ink:#0d0d0e;
    --white:#ffffff;
    --paper:#f6f6f6;
    --field:#d6d6d6;
    --leaf:#3f9b2a;
    --leaf-light:#7cc142;
    --muted:#8a8a8a;
    --text:#1b1b1b;
  }
  *{box-sizing:border-box;margin:0;padding:0}
  html,body{width:1200px;height:3270px;overflow:hidden;background:var(--paper)}
  body{font-family:"Crimson Text",Georgia,serif;color:var(--text);position:relative}

  .page{position:relative;width:1200px;height:3270px;background:linear-gradient(180deg,#fafafa 0%,#f2f2f2 50%,#f7f7f7 100%)}

  /* hero */
  .hero{position:relative;height:760px;overflow:hidden;color:var(--white)}
  .hero__photo{position:absolute;inset:0;
    background:
      radial-gradient(ellipse 22% 60% at 72% 45%,rgba(200,215,225,.75),rgba(120,140,150,0) 70%),
      radial-gradient(ellipse 40% 40% at 12% 90%,#27461f 0%,rgba(20,40,18,0) 70%),
      radial-gradient(ellipse 35% 55% at 95% 70%,#1e3a18 0%,rgba(20,40,18,0) 70%),
      linear-gradient(180deg,#1b2a22 0%,#34503a 25%,#3d5058 55%,#2a3840 80%,#1a2420 100%);}
  .hero__photo::after{content:"";position:absolute;left:0;right:0;top:0;height:150px;background:linear-gradient(180deg,#0b0b0c 0%,rgba(11,11,12,.85) 55%,rgba(11,11,12,0) 100%)}

  .nav{position:absolute;top:0;left:0;right:0;height:110px;display:flex;align-items:center;justify-content:center;z-index:2}
  .nav__list{display:flex;align-items:center;list-style:none}
  .nav__link{font-family:"Crimson Text",serif;font-weight:700;font-size:11px;letter-spacing:.04em;color:var(--white);text-transform:uppercase;padding:6px 11px}
  .nav__list--left .nav__link{margin-right:34px}
  .nav__list--right .nav__link{margin-left:34px}
  .nav__link--active{border:1.5px solid var(--white)}
  .brand{text-align:center;margin:0 36px}
  .brand__name{font-family:"Montserrat",sans-serif;font-weight:600;font-size:38px;letter-spacing:.01em;line-height:1;color:var(--white)}
  .brand__tag{font-family:"Crimson Text",serif;font-size:10.5px;letter-spacing:.3em;margin-top:8px;color:#e6e6e6}
  .nav__search{margin-left:70px;width:24px;height:24px}

  .hero__copy{position:absolute;left:221px;top:205px;z-index:2}
  .hero__title{font-family:"Kaushan Script",cursive;font-weight:400;font-size:100px;line-height:1.05;letter-spacing:-.01em}
  .hero__lead{font-size:27px;line-height:1.45;margin-top:22px;width:470px}
  .btn{display:inline-flex;align-items:center;gap:10px;font-family:"Montserrat",sans-serif;font-weight:600;font-size:10.5px;letter-spacing:.02em;text-transform:uppercase;border-radius:20px;padding:9px 18px}
  .btn--light{background:var(--white);color:var(--ink);margin-top:34px}
  .btn--dark{background:var(--ink);color:var(--white)}

  .mosaic{position:absolute;inset:0;z-index:2}
  .tile{position:absolute;width:186px;height:186px;transform:rotate(45deg);border:5px solid var(--white);box-shadow:0 6px 18px rgba(0,0,0,.35)}
  .tile--hummingbird{left:858px;top:185px;background:linear-gradient(135deg,#a89a8e,#6f6259 60%,#c4b7ab)}
  .tile--hare{left:968px;top:315px;background:linear-gradient(135deg,#c07a3c,#7a5a3a 45%,#d7dde6 75%,#8e9db1)}
  .tile--gull{left:768px;top:372px;background:linear-gradient(135deg,#a77a3d,#c9a36a 50%,#8b6330)}

  .edge{position:absolute;left:0;width:1200px;display:block}
  .hero .edge{bottom:0;height:26px}

  /* section heads */
  .leaf{display:block;width:30px;height:20px;border-radius:0 100% 0 100%;background:linear-gradient(135deg,var(--leaf-light),var(--leaf))}
  .section-title{font-family:"Crimson Text",serif;font-weight:700;font-size:38px;letter-spacing:.01em;color:var(--ink);text-transform:uppercase;line-height:1}

  /* about */
  .about{position:relative;height:560px}
  .about__art{position:absolute;left:260px;top:95px;width:310px;height:310px;border-radius:50%;
    background:radial-gradient(circle at 50% 45%,#e0b070 0%,#b6813f 45%,#7d5226 100%);box-shadow:0 0 0 26px rgba(190,190,190,.25)}
  .about__body{position:absolute;left:676px;top:82px;width:360px}
  .about__body .section-title{margin-top:14px}
  .rule{width:78px;height:2px;background:var(--ink);margin:12px 0 22px}
  .about__text{font-size:11.5px;line-height:1.72;text-align:justify}
  .about__body .btn{margin-top:26px}

  /* gallery */
  .gallery{position:relative;height:760px;text-align:center}
  .gallery .leaf{margin:10px auto 10px}
  .gallery__intro{font-size:11.5px;line-height:1.6;width:760px;margin:18px auto 0}
  .gallery__grid{display:grid;grid-template-columns:repeat(4,184px);grid-auto-rows:144px;gap:8px;width:760px;margin:36px auto 0}
  .photo{display:block}
  .photo--wide{grid-column:span 2}
  .photo--owl{background:linear-gradient(135deg,#a07544,#6b4a28 50%,#b88c55)}
  .photo--gull{background:linear-gradient(160deg,#2a4f82,#4a74a8 55%,#1f3c66)}
  .photo--woodpecker{background:linear-gradient(160deg,#d8dee6,#b8a89a 60%,#6f5a48)}
  .photo--ducks{background:linear-gradient(180deg,#6a4a34,#2d3a42 60%,#15202a)}
  .photo--waxwing{background:linear-gradient(160deg,#c7d09a,#6a8a3a 55%,#394f22)}
  .photo--towhee{background:linear-gradient(160deg,#6e6058,#a89488 55%,#d8d2cc)}
  .gallery .btn{margin-top:36px;padding:9px 26px}

  /* contact */
  .contact{position:relative;height:680px}
  .contact__photo{position:absolute;left:221px;top:40px;width:372px;height:376px;background:linear-gradient(170deg,#cfc6c0 0%,#b46a35 40%,#c47a40 60%,#e8e6e6 100%)}
  .contact__form{position:absolute;left:610px;top:22px;width:380px}
  .contact__form .section-title{font-size:34px;margin:8px 0 18px}
  .field{display:block;width:100%;height:36px;background:var(--field);margin-bottom:14px;font-family:"Crimson Text",serif;font-weight:700;font-size:9.5px;letter-spacing:.04em;text-transform:uppercase;padding:12px 14px;color:var(--ink)}
  .field--message{height:108px}
  .submit{display:inline-block;background:var(--ink);color:var(--white);font-family:"Crimson Text",serif;font-weight:700;font-size:12px;letter-spacing:.1em;text-transform:uppercase;padding:11px 32px}

  /* footer */
  .footer{position:absolute;left:0;right:0;bottom:0;height:510px;background:var(--ink);color:var(--white);text-align:center}
  .footer .edge{top:-22px;height:24px}
  .contacts{display:flex;justify-content:center;padding-top:86px}
  .contact-item{display:flex;align-items:center;gap:14px;text-align:left;padding:0 34px;border-right:1px solid #3a3a3a;height:70px}
  .contact-item:last-child{border-right:0}
  .contact-item__icon{width:50px;height:50px;border:2px solid var(--white);border-radius:50%;display:flex;align-items:center;justify-content:center;flex:none}
  .contact-item__label{font-family:"Kaushan Script",cursive;font-size:17px;line-height:1.2}
  .contact-item__value{font-size:11px;line-height:1.45;margin-top:6px}
  .footer .brand{margin-top:58px}
  .social{display:flex;justify-content:center;gap:28px;margin-top:24px;list-style:none}
  .social__dot{width:12px;height:12px;border-radius:50%;background:#cfcfcf;display:block}
  .footer-nav{display:flex;justify-content:center;gap:40px;list-style:none;margin-top:30px;font-size:11px;text-transform:uppercase}
  .copyright{font-size:10px;color:var(--muted);margin-top:30px}
</style>
</head>
<body>
<div class="page">

  <header class="hero">
    <div class="hero__photo" role="img" aria-label="Photograph of a waterfall pouring between moss-covered cliffs"></div>

    <nav class="nav">
      <ul class="nav__list nav__list--left">
        <li><span class="nav__link nav__link--active">Home</span></li>
        <li><span class="nav__link">Portfolio</span></li>
        <li><span class="nav__link" style="margin-right:0">About</span></li>
      </ul>
      <div class="brand">
        <div class="brand__name">NORA FALKETT</div>
        <div class="brand__tag">WILDLIFE PHOTOGRAPHER</div>
      </div>
      <ul class="nav__list nav__list--right">
        <li><span class="nav__link" style="margin-left:0">Gallery</span></li>
        <li><span class="nav__link">Contact</span></li>
      </ul>
      <svg class="nav__search" viewBox="0 0 24 24" fill="none" stroke="#fff" stroke-width="1.6" aria-label="Search"><circle cx="10" cy="10" r="7"/><line x1="15" y1="15" x2="22" y2="22"/></svg>
    </nav>

    <div class="hero__copy">
      <h1 class="hero__title">Lorem Ipsum</h1>
      <p class="hero__lead">Lorem Ipsum is simply dummy text of the printing and typesetting industry</p>
      <span class="btn btn--light">Know More
        <svg width="11" height="10" viewBox="0 0 11 10"><path d="M0 5h9M5.5 1.5 9 5 5.5 8.5" fill="none" stroke="#0d0d0e" stroke-width="1.8"/></svg></span>
    </div>

    <div class="mosaic">
      <div class="tile tile--hummingbird" role="img" aria-label="Photograph of a hummingbird in flight"></div>
      <div class="tile tile--hare" role="img" aria-label="Photograph of a hare running across snow"></div>
      <div class="tile tile--gull" role="img" aria-label="Photograph of a gull gliding over dry grass"></div>
    </div>

    <svg class="edge" viewBox="0 0 1200 26" preserveAspectRatio="none" aria-hidden="true">
      <polygon fill="#fafafa" points="0,12 40,8 80,14 130,6 180,13 240,9 300,15 360,7 420,12 480,8 540,14 600,9 660,13 720,6 780,12 840,8 900,14 960,7 1020,13 1080,9 1140,14 1200,8 1200,26 0,26"/>
    </svg>
  </header>

  <section class="about">
    <div class="about__art" role="img" aria-label="Photograph of a small olive songbird perched on a twig, framed in a painted splash"></div>
    <div class="about__body">
      <span class="leaf" role="img" aria-label="Leaf ornament"></span>
      <h2 class="section-title">About Us</h2>
      <div class="rule"></div>
      <p class="about__text">Lorem Ipsum is simply dummy text of the printing and typesetting industry. Lorem Ipsum has been the industry's standard dummy text ever since the 1500s, when an unknown printer took a galley of type and scrambled it to make a type specimen book. It has survived not only five centuries, but also the leap into electronic typesetting, remaining essentially unchanged. It was popularised in the 1960s with the release of transfer sheets containing Lorem Ipsum passages, and more recently with desktop publishing and layout software including versions of Lorem Ipsum.</p>
      <span class="btn btn--dark">Read More
        <svg width="11" height="10" viewBox="0 0 11 10"><path d="M0 5h9M5.5 1.5 9 5 5.5 8.5" fill="none" stroke="#fff" stroke-width="1.8"/></svg></span>
    </div>
  </section>

  <section class="gallery">
    <span class="leaf" role="img" aria-label="Leaf ornament"></span>
    <h2 class="section-title">Our Gallery</h2>
    <p class="gallery__intro">Lorem Ipsum is simply dummy text of the printing and typesetting industry. Lorem Ipsum has been the industry's standard dummy text ever since the 1500s, when an unknown printer took a galley of type and scrambled it to make a type specimen book.</p>
    <div class="gallery__grid">
      <span class="photo photo--wide photo--owl" role="img" aria-label="Photograph of an owl flying low over a golden field"></span>
      <span class="photo photo--gull" role="img" aria-label="Photograph of a gull diving over blue water"></span>
      <span class="photo photo--woodpecker" role="img" aria-label="Photograph of a red-headed woodpecker on a branch"></span>
      <span class="photo photo--ducks" role="img" aria-label="Photograph of two hooded mergansers on water"></span>
      <span class="photo photo--waxwing" role="img" aria-label="Photograph of waxwings in an evergreen"></span>
      <span class="photo photo--wide photo--towhee" role="img" aria-label="Photograph of a towhee perched on a log"></span>
    </div>
    <span class="btn btn--dark">View All
      <svg width="11" height="10" viewBox="0 0 11 10"><path d="M0 5h9M5.5 1.5 9 5 5.5 8.5" fill="none" stroke="#fff" stroke-width="1.8"/></svg></span>
  </section>

  <section class="contact">
    <div class="contact__photo" role="img" aria-label="Photograph of a red fox standing in snow"></div>
    <form class="contact__form">
      <span class="leaf" role="img" aria-label="Leaf ornament"></span>
      <h2 class="section-title">Get In Touch</h2>
      <span class="field">Name</span>
      <span class="field">Email</span>
      <span class="field">Phone</span>
      <span class="field field--message">Message</span>
      <span class="submit">Submit</span>
    </form>
  </section>

  <footer class="footer">
    <svg class="edge" viewBox="0 0 1200 24" preserveAspectRatio="none" aria-hidden="true">
      <polygon fill="#0d0d0e" points="0,24 0,12 30,16 60,8 95,14 130,6 170,15 210,9 250,13 290,5 330,14 370,10 410,16 450,7 490,13 530,9 570,15 610,6 650,12 690,8 730,15 770,10 810,14 850,6 890,13 930,9 970,15 1010,7 1050,12 1090,8 1130,15 1170,9 1200,13 1200,24"/>
    </svg>

    <div class="contacts">
      <div class="contact-item">
        <span class="contact-item__icon"><svg width="20" height="20" viewBox="0 0 24 24" fill="#fff"><path d="M6.6 10.8a15.1 15.1 0 0 0 6.6 6.6l2.2-2.2a1 1 0 0 1 1-.25 11.4 11.4 0 0 0 3.6.57 1 1 0 0 1 1 1V20a1 1 0 0 1-1 1A17 17 0 0 1 3 4a1 1 0 0 1 1-1h3.5a1 1 0 0 1 1 1c0 1.25.2 2.45.57 3.6a1 1 0 0 1-.25 1z"/></svg></span>
        <div><div class="contact-item__label">Phone number</div><div class="contact-item__value">(443) - 581 - 2094</div></div>
      </div>
      <div class="contact-item">
        <span class="contact-item__icon"><svg width="22" height="16" viewBox="0 0 22 16"><rect x="1" y="1" width="20" height="14" rx="2" fill="#fff"/><path d="M2 2l9 7 9-7" fill="none" stroke="#0d0d0e" stroke-width="1.6"/></svg></span>
        <div><div class="contact-item__label">Email address</div><div class="contact-item__value">infosupport@fernowlpix.com</div></div>
      </div>
      <div class="contact-item">
        <span class="contact-item__icon"><svg width="16" height="22" viewBox="0 0 16 22"><path d="M8 1a7 7 0 0 0-7 7c0 5 7 13 7 13s7-8 7-13a7 7 0 0 0-7-7z" fill="#fff"/><circle cx="8" cy="8" r="2.6" fill="#0d0d0e"/></svg></span>
        <div><div class="contact-item__label">Location</div><div class="contact-item__value">Head Office Address<br>4817 Maple Hollow Lane, Columbia MD</div></div>
      </div>
    </div>

    <div class="brand">
      <div class="brand__name">NORA FALKETT</div>
      <div class="brand__tag">WILDLIFE PHOTOGRAPHER</div>
    </div>

    <ul class="social" aria-label="Social links">
      <li><span class="social__dot"></span></li>
      <li><span class="social__dot"></span></li>
      <li><span class="social__dot"></span></li>
      <li><span class="social__dot"></span></li>
    </ul>

    <ul class="footer-nav">
      <li>Home</li><li>Portfolio</li><li>About</li><li>Gallery</li><li>Contact</li>
    </ul>

    <p class="copyright">Copyright 2021 NORA FALKETT. All Rights Are Reserved.</p>
  </footer>

</div>
</body>
</html>
```